Korvane Plumbing Business cards

Company is Korvane Plumbing.
name Dorian Malvessey, I am a plumber, drainer, gasfitter and roofer
Mobile: 0461 590 314
Email address: info@korvaneplumbing.example (check out my website for some ideas)
Website: www.korvaneplumbing.example
ABN: 42 198 603 771
LIC: 516042D

I am reliable all round plumber. I am a 24 hour emergency service. Korvane Plumbing is a professional plumbing service in the Illawarra, South Coast, Southern Sydney and Southern Highland regions of NSW. We offer a 24 hour emergency service for piece of mind to our customers. Call us now to see how we can help you. Korvane Plumbing approaches every job with attention to detail and excellent customer service. With our superior workmanship you can be confident that the job will be done right the first time around. You can rest assured with results that are guaranteed to last.

Target Market(s)

the general public

Contact Information for Business Card

look up website for some ideas something with similar colours to logo and new modern and to catch the eye.

Colors
fdfdfd
ffffff
000000
7f7f7f
aaaaaa
33a6d7
0492cd

Requirements
Must have
• all contact details
• company- Korvane Plumbing
• name- Dorian Malvessey
• number mobile- 0461 590 314
• Email address- info@korvaneplumbing.example
• Website- www.korvaneplumbing.example
• ABN- 42 198 603 771
• LIC- 516042D

```html
<!DOCTYPE html>
<html lang="en">
<head>
<meta charset="utf-8">
<title>Korvane Plumbing – Business Cards</title>
<link href="https://fonts.googleapis.com/css2?family=Lato:wght@400;700&display=swap" rel="stylesheet">
<style>
  :root {
    --stage: #1a1a1a;
    --card-dark: #232323;
    --ink-black: #000000;
    --paper: #ffffff;
    --grey: #7f7f7f;
    --grey-light: #aaaaaa;
    --blue: #0492cd;
    --blue-soft: #33a6d7;
  }
  * { margin: 0; padding: 0; box-sizing: border-box; }
  html, body { width: 1200px; height: 912px; overflow: hidden; background: var(--stage); }
  body { font-family: "Lato", sans-serif; }
  .canvas {
    width: 1200px; height: 912px;
    display: flex; flex-direction: column; align-items: center; justify-content: center; gap: 36px;
  }
  .card {
    position: relative; width: 700px; height: 400px; overflow: hidden;
    box-shadow: 0 10px 30px rgba(0,0,0,.5);
  }
  /* back card */
  .card-back { background: var(--card-dark); }
  .back-name {
    position: absolute; left: 0; right: 0; top: 150px; text-align: center;
    color: var(--blue); font-weight: 700; font-size: 46px; letter-spacing: 2px; text-transform: uppercase;
  }
  .back-web {
    position: absolute; left: 0; right: 0; top: 300px; text-align: center;
    color: var(--paper); font-size: 20px; letter-spacing: .5px;
  }
  /* front card */
  .card-front { background: var(--card-dark); }
  .card-front svg.swoosh { position: absolute; inset: 0; }
  .front-name {
    position: absolute; left: 40px; top: 80px;
    color: var(--blue); font-weight: 700; font-size: 34px; letter-spacing: 2px; text-transform: uppercase; line-height: 1.15;
    white-space: nowrap;
  }
  .person { position: absolute; right: 40px; top: 186px; text-align: right; }
  .person-name { color: var(--blue); font-weight: 700; font-size: 26px; line-height: 1.1; }
  .person-role { color: var(--paper); font-size: 16px; margin-top: 2px; }
  .contacts { position: absolute; right: 40px; top: 262px; text-align: right; list-style: none; }
  .contacts li {
    color: var(--paper); font-size: 16px; line-height: 25px;
    display: flex; align-items: center; justify-content: flex-end; gap: 8px;
  }
  .contacts svg { width: 14px; height: 14px; }
  .registration { position: absolute; left: 40px; bottom: 30px; color: var(--paper); font-size: 21px; line-height: 27px; }
</style>
</head>
<body>
<main class="canvas">
  <section class="card card-back" aria-label="Card back">
    <p class="back-name">Korvane Plumbing</p>
    <p class="back-web">www.korvaneplumbing.example</p>
  </section>

  <section class="card card-front" aria-label="Card front">
    <svg class="swoosh" viewBox="0 0 700 400" aria-hidden="true">
      <path d="M0,0 H560 C510,30 470,90 420,150 C360,215 270,240 0,250 Z" fill="var(--paper)"/>
      <path d="M578,0 C528,32 488,95 436,158 C374,228 280,254 0,262" fill="none" stroke="var(--ink-black)" stroke-width="8"/>
      <path d="M606,0 C552,35 512,105 458,170 C394,245 295,272 0,282" fill="none" stroke="var(--blue)" stroke-width="11"/>
    </svg>

    <p class="front-name">Korvane Plumbing</p>

    <div class="person">
      <p class="person-name">Dorian Malvessey</p>
      <p class="person-role">Plumber</p>
    </div>

    <ul class="contacts">
      <li>0461 590 314
        <svg viewBox="0 0 14 14"><rect x="3.5" y="1" width="7" height="12" rx="1.5" fill="none" stroke="var(--blue)" stroke-width="1.3"/></svg>
      </li>
      <li>info@korvaneplumbing.example
        <svg viewBox="0 0 14 14"><rect x="1" y="3" width="12" height="8" fill="var(--blue)"/><path d="M1,3 L7,8 L13,3" fill="none" stroke="var(--paper)" stroke-width="1"/></svg>
      </li>
      <li>www.korvaneplumbing.example
        <svg viewBox="0 0 14 14"><circle cx="7" cy="7" r="6" fill="var(--blue)"/><path d="M1,7 H13 M7,1 C4,4 4,10 7,13 M7,1 C10,4 10,10 7,13" fill="none" stroke="var(--paper)" stroke-width=".8"/></svg>
      </li>
    </ul>

    <p class="registration">ABN- 42 198 603 771<br>LIC- 516042D</p>
  </section>
</main>
</body>
</html>
```